Design a double sided business card

We are looking for a clean, eye-catching, and contemporary design that enhances the brand and presents a premium, professional image. Our preference is for a brown card with black gloss detailing and embossed elements; however, we are open to creative input and design suggestions that best achieve a strong visual impact.

Please see the attached existing business card for reference. We use both black and brown colours consistently across our branding.

On sample provided

```html
<!DOCTYPE html>
<html lang="en">
<head>
<meta charset="UTF-8">
<title>Korvan – Business Card</title>
<link href="https://fonts.googleapis.com/css2?family=Montserrat:wght@700;800&family=Roboto:wght@400;500&display=swap" rel="stylesheet">
<style>
  :root {
    --stage: #2b2b2d;
    --sand: #c8b39a;
    --ink: #0c0c0c;
    --sand-light: #d9c8b2;
    --paper: #f4f1ec;
  }
  * { box-sizing: border-box; margin: 0; padding: 0; }
  html, body {
    width: 1200px; height: 880px; overflow: hidden;
    background: var(--stage);
  }
  .canvas { position: relative; width: 1200px; height: 880px; }
  .card {
    position: absolute; width: 640px; height: 370px;
    border-radius: 26px; overflow: hidden;
    background: var(--sand);
  }
  .card--front { left: 120px; top: 45px; }
  .card--back { left: 440px; top: 465px; }

  .brand {
    position: absolute; display: flex; flex-direction: column; align-items: center; gap: 18px;
  }
  .brand__square {
    width: 70px; height: 70px; background: var(--ink);
  }
  .brand__name {
    font-family: "Montserrat", sans-serif; font-weight: 800;
    color: var(--ink); letter-spacing: 0.14em;
  }
  .card--front .brand { left: 0; right: 0; top: 92px; }
  .card--front .brand__name { font-size: 62px; }
  .card--back .brand { left: 44px; top: 128px; gap: 14px; }
  .card--back .brand__square { width: 56px; height: 56px; }
  .card--back .brand__name { font-size: 46px; }

  .back__panel { position: absolute; inset: 0; width: 100%; height: 100%; }

  .contact {
    position: absolute; left: 376px; top: 52px; width: 250px;
    font-family: "Roboto", sans-serif; color: var(--paper);
  }
  .contact__name {
    font-family: "Montserrat", sans-serif; font-weight: 700;
    font-size: 24px; color: var(--sand); letter-spacing: 0.02em;
  }
  .contact__role { font-size: 13px; color: #bdbdbd; margin-top: 4px; }
  .contact__address { font-size: 16px; line-height: 1.4; margin-top: 20px; }
  .contact__list { list-style: none; margin-top: 22px; font-size: 16px; }
  .contact__list li { display: flex; align-items: center; gap: 12px; height: 26px; }
  .contact__list svg { width: 15px; height: 15px; flex: none; fill: var(--sand); }
</style>
</head>
<body>
<main class="canvas">
  <section class="card card--front" aria-label="Card front">
    <div class="brand">
      <span class="brand__square"></span>
      <span class="brand__name">KORVAN</span>
    </div>
  </section>

  <section class="card card--back" aria-label="Card back">
    <svg class="back__panel" viewBox="0 0 640 370" preserveAspectRatio="none" aria-hidden="true">
      <path d="M240 0 C 330 60, 360 200, 350 370 L640 370 L640 0 Z" fill="#0c0c0c"/>
      <path d="M228 0 C 318 60, 346 200, 336 370" fill="none" stroke="#d9c8b2" stroke-width="3"/>
      <path d="M232 0 C 326 62, 354 200, 343 370 L352 370 C 362 200, 332 60, 244 0 Z" fill="#0c0c0c"/>
    </svg>

    <div class="brand">
      <span class="brand__square"></span>
      <span class="brand__name">KORVAN</span>
    </div>

    <div class="contact">
      <h1 class="contact__name">RAVI MARSH</h1>
      <p class="contact__role">Director</p>
      <p class="contact__address">The Green Willow Lane<br>Eastbridge UB9 4KT</p>
      <ul class="contact__list">
        <li><svg viewBox="0 0 24 24"><path d="M6.6 10.8a15 15 0 0 0 6.6 6.6l2.2-2.2a1 1 0 0 1 1-.25 11.4 11.4 0 0 0 3.6.57 1 1 0 0 1 1 1V20a1 1 0 0 1-1 1A17 17 0 0 1 3 4a1 1 0 0 1 1-1h3.5a1 1 0 0 1 1 1c0 1.25.2 2.45.57 3.57a1 1 0 0 1-.25 1z"/></svg>0800 555 0142</li>
        <li><svg viewBox="0 0 24 24"><path d="M7 1h10a2 2 0 0 1 2 2v18a2 2 0 0 1-2 2H7a2 2 0 0 1-2-2V3a2 2 0 0 1 2-2zm0 3v15h10V4z"/></svg>07700900318</li>
        <li><svg viewBox="0 0 24 24"><path d="M2 5h20v14H2zm2 2v.5l8 5 8-5V7z"/></svg>ravi@korvan.co.uk</li>
        <li><svg viewBox="0 0 24 24"><circle cx="12" cy="12" r="10"/></svg>www.korvan.co.uk</li>
      </ul>
    </div>
  </section>
</main>
</body>
</html>
```